Bluebrook Irrigation Business Card and Stationary
Business Cards, Envelopes, Stationary, etc.
Simple
Doug Harlan
General Operations Manager
742 Orchard Lane
Irving, TX 75119
doug@irrigatepros.com
www.irrigatepros.com
Li 48391
I want the inside part to list services that we perform.
1. Lawn Sprinkler Repair
2. Lawn Sprinkler Installation
3. Sprinkler System Efficiency Evaluation
4. French/Area Drains
5. Outdoor Lighting
6. Tree/Shrub Planting
7. Landscaping
8. Water Features
9. Sod
10. Backflow Testing
11. Outdoor/Landscape Lighting
12. Soil Test/Analysis
Arrange all of the information as you feel it fits best. I am also getting a PO box today, so the address will e different. I will update that when I have the info. Also, I would like a sticker that we can put on the customers controllers, about business card size that says "call for service," and then has our phone #. I am not opposed to having perfectly rectangular business cards, but am also not sold on it, maybe something with rounded corners.

```html
<!DOCTYPE html>
<html lang="en">
<head>
<meta charset="utf-8">
<title>Bluebrook Irrigation Business Cards</title>
<link href="https://fonts.googleapis.com/css2?family=Roboto+Condensed:wght@400;700&display=swap" rel="stylesheet">
<style>
  :root {
    --stage: #e9e6e1;
    --card-white: #ffffff;
    --wash-blue: #cfe6f6;
    --back-light: #6fa3d6;
    --back-dark: #2f6aa5;
    --brand-green: #8cc63f;
    --name-green: #2e9a4e;
    --text-blue: #2f6fa8;
    --text-dark: #3a4a57;
    --mark-blue: #3f86c9;
  }
  * { margin: 0; padding: 0; box-sizing: border-box; }
  html, body { width: 1200px; height: 901px; overflow: hidden; }
  body {
    background: var(--stage);
    font-family: "Roboto Condensed", Arial, sans-serif;
    position: relative;
  }
  .card {
    position: absolute;
    width: 500px;
    height: 288px;
    overflow: hidden;
    box-shadow: 0 6px 18px rgba(0,0,0,.18);
  }
  .card--rounded { border-radius: 26px; }
  .card--front {
    background: linear-gradient(160deg, var(--card-white) 45%, var(--wash-blue) 100%);
  }
  .card--back {
    background: radial-gradient(ellipse at 50% 30%, var(--back-light) 0%, var(--back-dark) 95%);
  }
  .pos-tl { left: 80px;  top: 61px; }
  .pos-tr { left: 646px; top: 61px; }
  .pos-bl { left: 80px;  top: 541px; }
  .pos-br { left: 650px; top: 541px; }

  .contact { position: absolute; left: 40px; top: 82px; color: var(--text-blue); }
  .contact__name { font-weight: 700; font-size: 17px; color: var(--name-green); }
  .contact__title { font-weight: 700; font-size: 10px; color: var(--text-dark); margin-top: 1px; }
  .contact__address { margin-top: 30px; font-size: 10.5px; line-height: 13px; font-weight: 700; }
  .contact__grid { display: grid; grid-template-columns: 44px auto; font-size: 10.5px; line-height: 13px; font-weight: 700; }
  .contact__web { position: absolute; left: 40px; top: 244px; font-size: 13px; font-weight: 700; color: var(--text-dark); }

  .brand { position: absolute; text-align: center; }
  .brand--front { left: 230px; top: 22px; width: 250px; }
  .brand--back { left: 0; top: 40px; width: 500px; }
  .brand__dot { display: block; margin: 0 auto; border-radius: 50%; background: var(--mark-blue); }
  .brand--front .brand__dot { width: 44px; height: 44px; }
  .brand--back .brand__dot { width: 70px; height: 70px; background: #ffffff; opacity: .9; }
  .brand__name { font-weight: 700; color: var(--brand-green); text-transform: uppercase; letter-spacing: .5px; }
  .brand--front .brand__name { font-size: 19px; margin-top: 8px; }
  .brand--back .brand__name { font-size: 34px; margin-top: 22px; }
  .brand__tagline { font-weight: 700; text-transform: uppercase; }
  .brand--front .brand__tagline { font-size: 7.5px; color: var(--text-blue); }
  .brand--back .brand__tagline { font-size: 11.5px; color: #ffffff; }
  .brand__since { font-weight: 700; }
  .brand--front .brand__since { font-size: 8.5px; color: var(--text-blue); }
  .brand--back .brand__since { font-size: 15px; color: #ffffff; margin-top: 2px; }
</style>
</head>
<body>

<section class="card card--front pos-tl">
  <div class="contact">
    <div class="contact__name">Doug Harlan</div>
    <div class="contact__title">General Operations Manager</div>
    <div class="contact__address">742 Orchard Lane<br>Irving, TX 75119</div>
    <div class="contact__grid">
      <span>Phone:</span><span>555.010.2588</span>
      <span>Cell:</span><span>555.010.4833</span>
      <span>Fax:</span><span>555.010.7553</span>
      <span>Email:</span><span>doug@irrigatepros.com</span>
    </div>
  </div>
  <div class="contact__web">www.irrigatepros.com</div>
  <div class="brand brand--front">
    <span class="brand__dot"></span>
    <div class="brand__name">Bluebrook Irrigation</div>
    <div class="brand__tagline">Providing quality lawn sprinkler solutions to DFW</div>
    <div class="brand__since">SINCE 1985</div>
  </div>
</section>

<section class="card card--back pos-tr">
  <div class="brand brand--back">
    <span class="brand__dot"></span>
    <div class="brand__name">Bluebrook Irrigation</div>
    <div class="brand__tagline">Providing quality lawn sprinkler solutions to DFW</div>
    <div class="brand__since">SINCE 1985</div>
  </div>
</section>

<section class="card card--front card--rounded pos-bl">
  <div class="contact">
    <div class="contact__name">Doug Harlan</div>
    <div class="contact__title">General Operations Manager</div>
    <div class="contact__address">742 Orchard Lane<br>Irving, TX 75119</div>
    <div class="contact__grid">
      <span>Phone:</span><span>555.010.2588</span>
      <span>Cell:</span><span>555.010.4833</span>
      <span>Fax:</span><span>555.010.7553</span>
      <span>Email:</span><span>doug@irrigatepros.com</span>
    </div>
  </div>
  <div class="contact__web">www.irrigatepros.com</div>
  <div class="brand brand--front">
    <span class="brand__dot"></span>
    <div class="brand__name">Bluebrook Irrigation</div>
    <div class="brand__tagline">Providing quality lawn sprinkler solutions to DFW</div>
    <div class="brand__since">SINCE 1985</div>
  </div>
</section>

<section class="card card--back card--rounded pos-br">
  <div class="brand brand--back">
    <span class="brand__dot"></span>
    <div class="brand__name">Bluebrook Irrigation</div>
    <div class="brand__tagline">Providing quality lawn sprinkler solutions to DFW</div>
    <div class="brand__since">SINCE 1985</div>
  </div>
</section>

</body>
</html>
```